Stationary & Business Cards
TRB Weddings & Events by Greta
You need to extend the project before designers can submit more proposals, right now it is locked. Thank you! :)
And we need business cards, stationary & envelopes.
They like a zen feel...cherry blossoms...birds...
Thank you for all of your submissions. The owners do not like the purple logo anymore and have completly changed it. We have uploaded a eps file for it. This project is guaranteed and we will be picking a winner. If you have time please submit new designs. Thank you.
Your eps file is an image please upload orignal Ai file.
-Thanks
Please upload ai or eps of your logo.

```html
<!DOCTYPE html>
<html lang="en">
<head>
<meta charset="utf-8">
<title>TRB Weddings &amp; Events by Greta – Stationery</title>
<link rel="stylesheet" href="https://fonts.googleapis.com/css2?family=Questrial&display=swap">
<style>
  :root {
    --leaf: #a9cf5b;
    --ink: #3a3a3a;
    --paper: #ffffff;
    --edge: #9a9a9a;
    --backdrop: #ffffff;
  }
  * { box-sizing: border-box; margin: 0; padding: 0; }
  html, body { width: 1200px; height: 1101px; overflow: hidden; background: var(--backdrop); }
  body { position: relative; font-family: "Questrial", "Century Gothic", sans-serif; color: var(--ink); }

  .sheet { position: absolute; background: var(--paper); border: 1px solid var(--edge); box-shadow: 2px 2px 3px rgba(0,0,0,.15); }

  .monogram {
    position: absolute; background: var(--leaf); border-radius: 10%;
    display: flex; align-items: center; justify-content: center;
    color: var(--paper); letter-spacing: .04em;
  }
  .monogram--light { background: var(--paper); color: var(--leaf); }

  .tagline { position: absolute; width: 100%; text-align: center; }

  /* Letterhead */
  .letterhead { left: 39px; top: 15px; width: 807px; height: 1059px; }
  .letterhead .monogram { left: 347px; top: 45px; width: 111px; height: 111px; font-size: 40px; }
  .letterhead .tagline { top: 166px; font-size: 13px; }
  .letterhead__footer { position: absolute; left: 22px; bottom: 20px; font-size: 12px; white-space: nowrap; }
  .letterhead__footer .sep { color: var(--leaf); margin: 0 4px; }
  .letterhead__footer .web { color: var(--leaf); margin-left: 120px; }
  .letterhead__band { position: absolute; left: 0; right: 0; bottom: 0; height: 7px; background: var(--leaf); }

  /* Business card front */
  .card-front { left: 864px; top: 15px; width: 321px; height: 189px; text-align: center; }
  .card-front__name { position: absolute; top: 16px; width: 100%; color: var(--leaf); font-size: 13px; }
  .card-front__role { position: absolute; top: 34px; width: 100%; font-size: 9px; }
  .card-front .monogram { left: 138px; top: 54px; width: 45px; height: 45px; font-size: 15px; }
  .card-front .tagline { top: 104px; font-size: 7px; }
  .card-front__contact { position: absolute; top: 136px; width: 100%; font-size: 8px; line-height: 14px; }
  .card-front__contact .sep { color: var(--leaf); margin: 0 3px; }

  /* Business card back */
  .card-back { left: 864px; top: 219px; width: 321px; height: 171px; background: var(--leaf); border-color: var(--leaf); }
  .card-back .monogram { left: 138px; top: 63px; width: 45px; height: 45px; font-size: 15px; }

  /* Envelope */
  .envelope { position: absolute; left: 429px; top: 486px; width: 756px; height: 465px; }
  .envelope__flap { position: absolute; left: 0; top: 0; width: 756px; height: 154px; display: block; }
  .envelope__body { position: absolute; left: 0; top: 153px; width: 756px; height: 312px; background: var(--paper); border: 1px solid var(--edge); box-shadow: 2px 2px 3px rgba(0,0,0,.15); }
  .envelope__flap-mark { left: 361px; top: 14px; width: 34px; height: 34px; font-size: 11px; }
  .envelope__body .monogram { left: 322px; top: 33px; width: 111px; height: 111px; font-size: 40px; }
  .envelope__body .tagline { top: 152px; font-size: 13px; }
  .envelope__address { position: absolute; top: 260px; width: 100%; text-align: center; font-size: 12px; }
</style>
</head>
<body>

  <section class="sheet letterhead" aria-label="Letterhead">
    <div class="monogram">TRB</div>
    <p class="tagline">Weddings &amp; Events by Greta</p>
    <p class="letterhead__footer">Harbor Point, CA<span class="sep">|</span>555-014-2290 greta@trbweddingsandevents.com<span class="web">www.trbweddingsandevents.com</span></p>
    <div class="letterhead__band"></div>
  </section>

  <section class="sheet card-front" aria-label="Business card front">
    <p class="card-front__name">Greta Halden</p>
    <p class="card-front__role">Event Consultant</p>
    <div class="monogram">TRB</div>
    <p class="tagline">Weddings &amp; Events by Greta</p>
    <p class="card-front__contact">Harbor Point, CA<span class="sep">|</span>555-014-2290<br>greta@trbweddingsandevents.com<span class="sep">|</span>www.trbweddingsandevents.com</p>
  </section>

  <section class="sheet card-back" aria-label="Business card back">
    <div class="monogram monogram--light">TRB</div>
  </section>

  <section class="envelope" aria-label="Envelope">
    <svg class="envelope__flap" viewBox="0 0 756 154" aria-hidden="true">
      <path d="M0,154 L0,122 Q378,-122 756,122 L756,154 Z" fill="var(--leaf)"/>
    </svg>
    <div class="monogram monogram--light envelope__flap-mark">TRB</div>
    <div class="envelope__body">
      <div class="monogram">TRB</div>
      <p class="tagline">Weddings &amp; Events by Greta</p>
      <p class="envelope__address">Harbor Point, CA</p>
    </div>
  </section>

</body>
</html>
```